Anzeigengestaltung für Stelleninserate
Zielgruppe
Wir sind ein in Europa führender Hersteller flexibler Verpackungen, überwiegend für die Branchen Nahrungsmittel, Tiernahrung und Hygiene. Als mittelständisches Familienunternehmen mit Sitz in Feldau entwickeln wir uns sehr dynamisch, haben eine flache Führungshierarchie und setzen auf Eigenverantwortung unserer Mitarbeiter.
Aufgabenstellung
DINA4, Design sollte so gestaltet werden, dass es danach selber in Word bearbeitet werden kann und der Text immer wieder erneuert werden kann, es sollte nur eine Vorlage werden, und auf jegliche Stellenanzeigen anwendbar sein (siehe Anhang), eventuell auch Bilder austauschbar

```html
<!DOCTYPE html>
<html lang="de">
<head>
<meta charset="utf-8">
<title>Stelleninserat – Halmberg Verpackungstechnik</title>
<link href="https://fonts.googleapis.com/css2?family=Fira+Sans:wght@400;500;600;700&display=swap" rel="stylesheet">
<style>
  :root {
    --brand-blue: #2a63a2;
    --ink: #1d1d1f;
    --paper: #ffffff;
    --photo-light: #e9ecee;
    --photo-mid: #c9ced2;
    --photo-warm: #d8c79a;
    --facade-dark: #4a4f56;
    --facade-sky: #7ea3c9;
  }
  * { margin: 0; padding: 0; box-sizing: border-box; }
  html, body { width: 848px; height: 1200px; overflow: hidden; background: var(--paper); }
  body { font-family: "Fira Sans", sans-serif; color: var(--ink); }
  .ad { position: relative; width: 848px; height: 1200px; overflow: hidden; background: var(--paper); }

  .hero-photo {
    position: absolute; left: 0; top: 0; width: 848px; height: 403px;
    background: linear-gradient(160deg, var(--photo-light) 0%, var(--photo-mid) 45%, var(--photo-warm) 62%, var(--photo-light) 100%);
  }
  .logo-box {
    position: absolute; left: 476px; top: 27px; width: 346px; height: 84px;
    background: var(--paper); display: flex; align-items: center; justify-content: center;
  }
  .logo-name { font-weight: 700; font-size: 44px; letter-spacing: 1px; color: var(--brand-blue); }

  .headline-band {
    position: absolute; left: 0; top: 366px; width: 499px; height: 55px;
    background: var(--brand-blue); color: var(--paper);
    font-weight: 600; font-size: 35px; line-height: 55px; padding-left: 55px;
  }

  .content { position: absolute; left: 55px; top: 438px; width: 760px; }
  .intro { font-size: 14px; line-height: 21.3px; }
  .lead { font-weight: 500; font-size: 14.2px; margin-top: 20px; }
  .job-title { font-weight: 600; font-size: 23.5px; color: var(--brand-blue); margin-top: 6px; line-height: 32px; }
  .section-title { font-weight: 500; font-size: 14.2px; margin-top: 4px; }
  .list { list-style: none; font-size: 14px; line-height: 21.4px; margin-top: 7px; margin-bottom: 14px; }
  .list li { position: relative; padding-left: 19px; }
  .list li::before { content: "-"; position: absolute; left: 0; }
  .list.narrow { width: 440px; }

  .contact-box {
    position: absolute; left: 537px; top: 771px; width: 264px; height: 267px;
    border: 3px solid var(--brand-blue); text-align: center;
    font-size: 14px; line-height: 21.4px; padding-top: 21px;
  }
  .contact-company { font-weight: 500; color: var(--brand-blue); }
  .contact-gap { height: 21px; }

  .footer-band {
    position: absolute; left: 0; top: 1101px; width: 848px; height: 99px;
    background: var(--brand-blue); color: var(--paper);
    font-size: 14px; line-height: 21.4px; padding: 21px 0 0 55px;
  }
  .footer-text { width: 470px; }
  .footer-text strong { font-weight: 600; }

  .building-frame {
    position: absolute; left: 570px; top: 953px; width: 196px; height: 206px;
    background: var(--paper); padding: 0 8px 8px 8px;
  }
  .building-photo {
    width: 180px; height: 198px;
    background: linear-gradient(180deg, var(--facade-sky) 0%, var(--facade-dark) 55%, #9aa0a4 100%);
  }
</style>
</head>
<body>
<main class="ad">
  <div class="hero-photo" role="img" aria-label="Produktionshalle mit Druck- und Kaschiermaschinen sowie Folienrollen"></div>
  <div class="logo-box"><span class="logo-name">HALMBERG</span></div>

  <h1 class="headline-band">Wir suchen Verstärkung</h1>

  <section class="content">
    <p class="intro">Wir sind ein in Europa führender Hersteller flexibler Verpackungen, überwiegend für die Branchen Nahrungsmittel, Tiernahrung und Hygiene. Als mittelständisches Familienunternehmen mit Sitz in Feldau entwickeln wir uns sehr dynamisch, haben eine flache Führungshierarchie und setzen auf Eigenverantwortung unserer Mitarbeiter.</p>
    <p class="lead">Kommen Sie in unser Team als</p>
    <h2 class="job-title">Mitarbeiter für Labor und Qualitätssicherung (m/w/d).</h2>

    <h3 class="section-title">Ihre Verantwortung bei uns:</h3>
    <ul class="list">
      <li>Durchführung von Qualitätsprüfungen für die Freigabe zur Auslieferung unserer Produkte</li>
      <li>Erstellung von QM-konformer bzw. nachvollziehbarer Dokumentation</li>
      <li>Überprüfung der Einhaltung von Hygiene-, Qualitäts- und Sicherheitsrichtlinien</li>
      <li>Erkennung und Meldung von Abweichungen der Vorgaben bzw. Qualitätsmängeln</li>
      <li>Sicherstellung der permanenten Betriebsbereitschaft unserer Prüfgeräte</li>
      <li>Bearbeitung von internen und externen Reklamationen</li>
      <li>Unterstützung bei der Durchführung von Projektarbeiten</li>
      <li>Erarbeitung von Verbesserungsvorschlägen</li>
      <li>Erstellen von Protokollen und Prüfberichten</li>
    </ul>

    <h3 class="section-title">Ihre Verantwortung bei uns:</h3>
    <ul class="list">
      <li>Abgeschlossene technische Ausbildung</li>
      <li>Selbstbewusstes Auftreten und Durchsetzungsvermögen</li>
      <li>Selbstständige und zielorientierte Arbeitsweise</li>
      <li>Teamfähige Persönlichkeit</li>
    </ul>

    <h3 class="section-title">Ihre Verantwortung bei uns:</h3>
    <ul class="list narrow">
      <li>Eigenverantwortliches Aufgabengebiet in einem dynamischen Umfeld und motivierten Team</li>
      <li>Mitarbeit in einem erfolgreich geführten Familienunternehmen</li>
      <li>Angenehmes Arbeitsumfeld</li>
      <li>Persönliche und fachliche Entwicklungsmöglichkeiten</li>
    </ul>
  </section>

  <aside class="contact-box">
    <p class="contact-company">Halmberg Verpackungstechnik GmbH</p>
    <p>Lindenweg 4 A - 6800 Feldau</p>
    <div class="contact-gap"></div>
    <p>+43 5500 10200</p>
    <p>+43 5500 10200 - 12</p>
    <p>karriere@halmberg.example</p>
    <p>www.halmberg.example</p>
  </aside>

  <footer class="footer-band">
    <p class="footer-text">Wir freuen uns über Ihre Bewerbung, welche Sie bitte direkt an <strong>karriere@halmberg.example</strong> senden, am liebsten heute noch, damit wir Sie möglichst rasch persönlich kennenlernen können.</p>
  </footer>

  <div class="building-frame">
    <div class="building-photo" role="img" aria-label="Firmengebäude mit dunkler Fassade vor blauem Himmel"></div>
  </div>
</main>
</body>
</html>
```